Tidewell Boat Covers Sew on Care Labels

We manufacture custom boat covers and the purpose of the labels are to give existing customers care and maintenance instructions and to draw attention from potential customers who may see the cover and look to the label to find our contact details. We require a professional design for sew on labels including our logo, maintenance instructions, phone number and website. The design should be easy to read obviously. The finished size of the labels will be approximately business card size. It will be printed in either black and white or navy and white. I am happy for the logo and fonts can be tweaked as required.

Target Market(s)

Existing customers. Potential new customers who may see the cover on another boat and check the label for our details.

Industry/Entity Type

Marine

Colors

Designer to choose only greyscale colors for use in the design.

Requirements
Must have
• Our logo, the logo can be tweaked as required. Easy to read instructions as provided. Phone number and website must be included. Black and white or navy and white.
Nice to have
• See above
Should not have
• Too much unnecessary detail.

```html
<!DOCTYPE html>
<html lang="en">
<head>
<meta charset="utf-8">
<title>Tidewell Boat Covers – Care Label</title>
<link rel="stylesheet" href="https://fonts.googleapis.com/css2?family=Roboto:ital,wght@0,400;0,500;0,900;1,900&family=Roboto+Condensed:ital,wght@0,800;1,700&display=swap">
<style>
  :root {
    --page-bg: #e4e4e4;
    --card-black: #000000;
    --photo-top: #4a4a4a;
    --photo-bottom: #9c9c9c;
    --white: #ffffff;
    --address-grey: #dddddd;
    --contact-grey: #c4c4c4;
    --care-grey: #a8a8a8;
    --rule-grey: #444444;
    --badge-ink: #000000;
  }
  * { margin: 0; padding: 0; box-sizing: border-box; }
  html, body {
    width: 1200px; height: 1200px; overflow: hidden;
    background: var(--page-bg);
  }
  .label-card {
    position: absolute; left: 60px; top: 240px;
    width: 1080px; height: 720px;
    background: var(--card-black);
    overflow: hidden;
  }
  .card-art { position: absolute; inset: 0; }
  .badge {
    position: absolute; left: 814px; top: 202px;
    width: 216px; height: 216px;
    display: flex; flex-direction: column; align-items: center; justify-content: center;
    color: var(--badge-ink); text-align: center;
    font-family: "Roboto", sans-serif; line-height: 1.05;
  }
  .badge-percent { font-style: italic; font-weight: 900; font-size: 34px; }
  .badge-country { font-weight: 900; font-size: 24px; letter-spacing: 0.5px; }
  .badge-note { font-weight: 400; font-size: 22px; }
  .brand {
    position: absolute; left: 0; right: 0; top: 384px;
    text-align: center;
    font-family: "Roboto Condensed", sans-serif; font-weight: 800;
    color: var(--white);
  }
  .brand-name { font-size: 96px; line-height: 0.95; letter-spacing: 1px; }
  .brand-sub { font-size: 36px; letter-spacing: 8px; line-height: 1.1; }
  .address {
    position: absolute; left: 0; right: 0; top: 530px;
    text-align: center;
    font-family: "Roboto Condensed", sans-serif; font-style: italic; font-weight: 700;
    font-size: 27px; color: var(--address-grey);
  }
  .contact {
    position: absolute; left: 0; right: 0; top: 568px;
    text-align: center;
    font-family: "Roboto", sans-serif; font-weight: 500;
    font-size: 44px; color: var(--contact-grey);
    word-spacing: 4px;
  }
  .contact-divider { margin: 0 18px; }
  .care {
    position: absolute; left: 90px; right: 90px; top: 646px;
    padding-top: 14px;
    border-top: 2px solid var(--rule-grey);
    text-align: center;
    font-family: "Roboto", sans-serif; font-weight: 400;
    font-size: 22px; color: var(--care-grey);
  }
  .care-title { font-weight: 500; color: var(--address-grey); margin-right: 8px; }
</style>
</head>
<body>
  <div class="label-card">
    <svg class="card-art" width="1080" height="720" viewBox="0 0 1080 720">
      <defs>
        <linearGradient id="photo-tone" x1="0" y1="0" x2="0" y2="1">
          <stop offset="0" stop-color="var(--photo-top)"/>
          <stop offset="1" stop-color="var(--photo-bottom)"/>
        </linearGradient>
        <linearGradient id="band-fade" x1="0" y1="0" x2="0" y2="1">
          <stop offset="0" stop-color="#000" stop-opacity="0"/>
          <stop offset="1" stop-color="#000" stop-opacity="0.6"/>
        </linearGradient>
      </defs>
      <rect class="photo-area" x="0" y="0" width="1080" height="400" fill="url(#photo-tone)"
            role="img" aria-label="Photo of a child climbing onto a boat's bimini cover under an open sky"/>
      <path d="M0 272 Q540 372 1080 272 L1080 322 Q540 422 0 322 Z" fill="url(#band-fade)"/>
      <path class="black-band" d="M0 318 Q540 418 1080 318 L1080 720 L0 720 Z" fill="var(--card-black)"/>
      <polygon class="badge-burst" transform="translate(922 310)" fill="var(--white)"
        points="108,0 90.3,17.9 99.8,41.3 76.5,51.2 76.4,76.4 51.2,76.5 41.3,99.8 17.9,90.3 0,108 -17.9,90.3 -41.3,99.8 -51.2,76.5 -76.4,76.4 -76.5,51.2 -99.8,41.3 -90.3,17.9 -108,0 -90.3,-17.9 -99.8,-41.3 -76.5,-51.2 -76.4,-76.4 -51.2,-76.5 -41.3,-99.8 -17.9,-90.3 0,-108 17.9,-90.3 41.3,-99.8 51.2,-76.5 76.4,-76.4 76.5,-51.2 99.8,-41.3 90.3,-17.9"/>
    </svg>

    <div class="badge">
      <span class="badge-percent">100%</span>
      <span class="badge-country">AUSTRALIAN</span>
      <span class="badge-note">made and</span>
      <span class="badge-note">owned</span>
    </div>

    <div class="brand">
      <div class="brand-name">TIDEWELL</div>
      <div class="brand-sub">BOAT COVERS</div>
    </div>

    <p class="address">48 Harbourline Rd Marlow Bay 3190, Victoria, Australia</p>
    <p class="contact">03 9555 0142<span class="contact-divider">|</span>www.tidewell.net.au</p>
    <p class="care"><span class="care-title">CARE:</span>Rinse with fresh water · Dry fully before storing · No harsh cleaners</p>
  </div>
</body>
</html>
```